Business Card Design

I need a business card for a new company based in Australia called "ClinoPath".

Its a cloud program for GPs that allows them to search for the specialist they require using a simple user friendly tool.

I would like the colours to match those in the program (the colours in the logo attached).

The final design should reflect the programs clarity, ease of use and professionalism.

Target Market(s)

GPs and other Health Professionals

Industry/Entity Type

Business

Contact Information for Business Card

ClinoPath; The Whole Consultant Index; Maren Tolhurst CEO; 0417385261; maren@clinopath.example; www.clinopath.example

Requirements
Must have
• Must have the logo attached; the web address and my name and phone number
Nice to have
• the slogan "The Whole Consultant Index"

```html
<!DOCTYPE html>
<html lang="en">
<head>
<meta charset="utf-8">
<title>ClinoPath Business Card</title>
<link href="https://fonts.googleapis.com/css2?family=Inter:wght@400;500&family=Open+Sans:wght@400;700&display=swap" rel="stylesheet">
<style>
  :root {
    --brand-blue: #00b3e3;
    --slate-grey: #8e9093;
    --stripe-grey: #efefef;
    --text-grey: #6d6e70;
    --card-white: #ffffff;
    --backdrop: #e9e9ec;
  }
  * { box-sizing: border-box; margin: 0; padding: 0; }
  html, body { width: 1200px; height: 800px; overflow: hidden; }
  body {
    background: var(--backdrop);
    display: flex;
    align-items: center;
    justify-content: center;
    gap: 40px;
  }
  .card {
    position: relative;
    width: 540px;
    height: 309px;
    background: var(--card-white);
    overflow: hidden;
    box-shadow: 0 10px 30px rgba(0,0,0,0.15);
  }
  .wordmark {
    font-family: "Inter", sans-serif;
    font-weight: 500;
    color: var(--brand-blue);
    letter-spacing: -0.03em;
    line-height: 1;
  }
  .tagline {
    font-family: "Inter", sans-serif;
    font-weight: 400;
    color: var(--slate-grey);
    line-height: 1;
  }

  /* Logo side */
  .card--logo .top-band {
    position: absolute; left: 0; right: 0; top: 0; height: 30px;
    background: var(--slate-grey);
  }
  .card--logo .brand-lockup {
    position: absolute; left: 0; right: 0; top: 82px;
    text-align: center;
  }
  .card--logo .wordmark { font-size: 84px; }
  .card--logo .tagline { font-size: 24px; margin-top: 4px; }
  .card--logo .bottom-band {
    position: absolute; left: 0; right: 0; bottom: 26px; height: 36px;
    background: var(--brand-blue);
  }

  /* Contact side */
  .card--contact .brand-lockup {
    position: absolute; right: 34px; top: 28px;
    text-align: right;
  }
  .card--contact .wordmark { font-size: 52px; }
  .card--contact .tagline { font-size: 15px; margin-top: 2px; }
  .name-band {
    position: absolute; left: 0; right: 0; top: 108px; height: 32px;
    background: var(--brand-blue);
    display: flex; align-items: center;
    padding-left: 30px;
    font-family: "Open Sans", sans-serif;
    color: var(--card-white);
  }
  .name-band .person { font-weight: 700; font-size: 19px; text-transform: uppercase; }
  .name-band .role { font-size: 11px; margin-left: 6px; margin-top: 6px; }
  .contact-list {
    position: absolute; left: 0; right: 0; top: 140px;
    list-style: none;
    font-family: "Open Sans", sans-serif;
    font-size: 11px;
    color: var(--text-grey);
  }
  .contact-list li {
    height: 22px; line-height: 22px; padding-left: 30px;
  }
  .contact-list li:nth-child(odd) { background: var(--stripe-grey); }
  .contact-stripes {
    position: absolute; left: 0; right: 0; top: 228px; height: 22px;
    background: var(--card-white);
  }
  .card--contact .bottom-band {
    position: absolute; left: 0; right: 0; bottom: 26px; height: 24px;
    background: var(--brand-blue);
  }
</style>
</head>
<body>
  <section class="card card--logo" aria-label="Business card front">
    <div class="top-band"></div>
    <div class="brand-lockup">
      <div class="wordmark">ClinoPath</div>
      <div class="tagline">The Whole Consultant Index</div>
    </div>
    <div class="bottom-band"></div>
  </section>

  <section class="card card--contact" aria-label="Business card back">
    <div class="brand-lockup">
      <div class="wordmark">ClinoPath</div>
      <div class="tagline">The Whole Consultant Index</div>
    </div>
    <div class="name-band">
      <span class="person">Maren Tolhurst</span><span class="role">CEO</span>
    </div>
    <ul class="contact-list">
      <li>your address just for extra information</li>
      <li>0417385261</li>
      <li>maren@clinopath.example</li>
      <li>www.clinopath.example</li>
    </ul>
    <div class="bottom-band"></div>
  </section>
</body>
</html>
```